・依頼の目的 / 概要
オリジナルテキストを作成するにあたって表紙のデザインをお願いしたい。

・本の紹介
オリジナルテキストは「問題・模範解答全て生徒が作成」する仕様となっています。
昨今の教材だと問題が与えられて答えを求めると言った一方通行の教材しかないので問題作成から生徒に行なってもらいたいと思い、このテキストを作成しました。
生徒自ら問題を作成して模範解答も作るので友達同士で交換し合うこともできる(プレゼント)機能も兼ね備えています。

・デザイン要望
テキストは従来のような在り来たりの中身ではないので表紙も「近未来」的な要素を含めて欲しい。一見すると「勉強用のテキスト」には見えない方が好ましいです

*テキストのデザインは添付ファイルを参照してください

その他何かご不明点がございましたらお気軽にご質問ください
よろしくお願い致します。

*追記です
「数学の」テキストだとお伝えしましたが今後のことも考えて
【教科は後から付け足すデザイン】でお願いしたいです
(教科名のところだけ空白にするようなイメージです)
よろしくお願いします!
*再度追記です
この教材を全国の学生さんに届けたいと思っているので
【学習塾VELK】という文字は表紙に入れないようにお願い致します。
(裏表紙の裏に記載予定です)
よろしくお願いします!

一見シンプルなデザインのように見えますが「デザインの意味にかけた想い」が自分の「想い」と重なったため選ばせていただきました。

どれも素晴らしいデザインで、選考に2日要しました。。
本当に素晴らしいデザインのご提案をありがとうございました。
教材は5教科全部作成する予定ですのでまた機会がありましたらご提案していただきたいです!

本当にありがとうございました!

```html
<!DOCTYPE html>
<html lang="ja">
<head>
<meta charset="UTF-8">
<title>BATTERY — Original Text Cover</title>
<link rel="stylesheet" href="https://fonts.googleapis.com/css2?family=Cinzel:wght@500&family=Roboto:wght@700&family=Noto+Sans+JP:wght@700&display=swap">
<style>
  :root {
    --navy: #1b3452;
    --navy-deep: #17304c;
    --blue: #1f72c6;
    --blue-light: #3a9ae6;
    --blue-mid: #1565b8;
    --white: #ffffff;
  }
  html, body {
    margin: 0;
    padding: 0;
    overflow: hidden;
    background: var(--navy);
  }
  .cover {
    position: relative;
    width: 851px;
    height: 1200px;
    overflow: hidden;
    background: var(--navy);
  }
  .cover__art {
    position: absolute;
    inset: 0;
    width: 851px;
    height: 1200px;
  }
  .series-label {
    position: absolute;
    left: 144px;
    top: 146px;
    margin: 0;
    font-family: "Roboto", Arial, sans-serif;
    font-weight: 700;
    font-size: 18px;
    letter-spacing: 0.5px;
    color: var(--white);
  }
  .title {
    position: absolute;
    left: 142px;
    top: 186px;
    margin: 0;
    font-family: "Cinzel", "Times New Roman", serif;
    font-weight: 500;
    font-size: 98px;
    line-height: 1;
    letter-spacing: 6px;
    color: var(--blue);
  }
  .title--reflection {
    top: 262px;
    transform: scaleY(-1);
    background: linear-gradient(to top, rgba(31,114,198,0.75) 0%, rgba(31,114,198,0.25) 55%, rgba(31,114,198,0) 100%);
    -webkit-background-clip: text;
    background-clip: text;
    color: transparent;
  }
  .subject {
    position: absolute;
    left: 146px;
    top: 778px;
    margin: 0;
    color: var(--blue);
  }
  .subject__ja {
    display: block;
    font-family: "Noto Sans JP", sans-serif;
    font-weight: 700;
    font-size: 32px;
    line-height: 1;
  }
  .subject__en {
    display: block;
    margin-top: 30px;
    font-family: "Roboto", Arial, sans-serif;
    font-weight: 700;
    font-size: 16px;
    letter-spacing: 1px;
  }
</style>
</head>
<body>
<main class="cover">
  <svg class="cover__art" viewBox="0 0 851 1200" xmlns="http://www.w3.org/2000/svg">
    <defs>
      <linearGradient id="texture-blue" x1="0" y1="0" x2="1" y2="1">
        <stop offset="0" stop-color="#3c9ce8"/>
        <stop offset="0.5" stop-color="#1f78cf"/>
        <stop offset="1" stop-color="#0f5aa8"/>
      </linearGradient>
    </defs>
    <rect class="backdrop" width="851" height="1200" fill="var(--navy)"/>
    <circle class="texture-field" cx="780" cy="560" r="650" fill="url(#texture-blue)" role="img" aria-label="Blue low-poly geometric texture"/>
    <circle class="ring ring--outer" cx="360" cy="150" r="560" fill="none" stroke="#2a86d8" stroke-opacity="0.45" stroke-width="40"/>
    <path class="white-band" d="M0 620 C200 660 420 650 600 600 C520 770 490 950 520 1118 C340 1108 160 1110 0 1128 Z" fill="var(--white)"/>
    <circle class="dark-disc" cx="360" cy="150" r="510" fill="var(--navy-deep)"/>
    <path class="bottom-arc" d="M0 1110 Q420 1070 851 990 V1200 H0 Z" fill="var(--blue-mid)"/>
    <path class="bottom-base" d="M0 1135 Q420 1100 851 1030 V1200 H0 Z" fill="var(--navy)"/>
  </svg>

  <p class="series-label">ORIGINAL TEXT</p>
  <h1 class="title">BATTERY</h1>
  <div class="title title--reflection" aria-hidden="true">BATTERY</div>

  <p class="subject">
    <span class="subject__ja">数学</span>
    <span class="subject__en">MATHEMATICS</span>
  </p>
</main>
</body>
</html>
```